Scrum Master & Agile IT Coach Needing Business Website

Hello, my name is Brent Holloway
I am a project manger, scrum master, & agile coach. I work with IT development teams on major projects for Fortune 500 companies . My project management business has a website and can be found here: www.tq-keystride.example

I have launched a new company, ALL focused on IT Agile Coaching, I am looking to have a website created for my new company - the name of the new company is: Pins and Dials - Agile IT Coaching and Training.
I have a logo and it is provided in the materials. I like to logo; I am open to different color pallets.

The website will have a total of 7 pages; I have content for 5 of the 7 pages prepared; the other 2 pages will say under construction.

Page 1 Who am I, What I do, My Experience
Demonstrated experience and progression from Scrum Master to
Program Manager to Coach

Page 2 Pins & Dials - Agile Team Coaching
teams working major IT projects, multiple months/years

Page 3 Coaching @ the Team Level

Page 4 Coaching @ the Program Level ; LYNQ BQR level

Pages 5 -6 Under Construction

Page 7 Presentations, Slide Decks, Reference Materials

Mentor Nook need to have this highlighted somewhere Monthly Blog
Updates

Industry/Entity Type

IT development

Coding

Coded - Design and coding required

Number of Pages Required

5+ page

Requirements
Must have
• the website must be bold - I want those who visit to remember coming to my coaching site
Nice to have
• nice to have will be a modern / futuristic website; I work with IT developers, I want a website they will like
Should not have
• should not be stiff - it should be professional but fun

```html
<!DOCTYPE html>
<html lang="en">
<head>
<meta charset="utf-8">
<title>Pins &amp; Dials - Agile Team Coaching</title>
<link href="https://fonts.googleapis.com/css2?family=Oswald:wght@500&family=Poppins:wght@400;500;600&display=swap" rel="stylesheet">
<style>
:root{
  --green:#1fc98e;
  --ink:#111;
  --text:#444;
  --navy:#1e3f66;
  --hero-a:#2f5a5c;
  --hero-b:#4d7a78;
  --soft:#f4f4f4;
  --dark:#222;
  --white:#fff;
}
*{margin:0;padding:0;box-sizing:border-box}
html,body{width:1200px;height:2518px;overflow:hidden}
body{font-family:'Poppins',sans-serif;color:var(--text);background:var(--white);position:relative}
.abs{position:absolute}
.header{top:0;left:0;width:1200px;height:106px;background:var(--white)}
.brand{left:86px;top:22px;display:flex;align-items:center;gap:12px;font-weight:600;font-size:38px;color:var(--navy)}
.brand-dot{width:40px;height:40px;border:3px solid var(--navy);border-radius:50%}
.nav{left:490px;top:32px;display:flex;gap:24px;font-size:16px;line-height:19px;color:#222}
.nav a{color:inherit;text-decoration:none}
.nav .active{color:var(--green)}
.hero{top:106px;left:0;width:1200px;height:434px;background:linear-gradient(90deg,var(--hero-a),var(--hero-b) 60%,#8aa7a3);clip-path:polygon(0 0,100% 0,100% 72%,0 100%)}
.hero-kicker{left:111px;top:180px;color:var(--green);font-size:23px}
.hero-title{left:111px;top:226px;font-family:'Oswald',sans-serif;font-weight:500;color:var(--white);font-size:56px;line-height:68px;text-transform:uppercase}
.eyebrow{width:1200px;left:0;text-align:center;color:var(--green);font-size:18px;font-weight:500;text-transform:uppercase}
.heading{width:1200px;left:0;text-align:center;font-family:'Oswald',sans-serif;font-weight:500;color:var(--ink);font-size:44px;text-transform:uppercase}
.card{background:var(--white);box-shadow:0 4px 20px rgba(0,0,0,.08)}
.photo{background:linear-gradient(135deg,#0b2a55,#1c6bb0 60%,#0c2345)}
.photo-light{background:linear-gradient(135deg,#d9dfe6,#a9b4c0 55%,#6f7b88)}
.card-title{font-size:26px;font-weight:500;color:var(--ink)}
.ticks{list-style:none;font-size:16.5px;color:#555}
.ticks li{display:flex;align-items:center;gap:9px;height:32.5px}
.ticks svg{flex:none}
.soft-band{left:0;top:1572px;width:1200px;height:560px;background:var(--soft);clip-path:polygon(0 15%,100% 0,100% 100%,0 100%)}
.role{display:flex;align-items:center;gap:34px;padding:0 22px;border-radius:10px;background:var(--white);box-shadow:0 4px 18px rgba(0,0,0,.07)}
.role p{font-size:23px;line-height:33px;color:#333}
.footer{left:0;top:2032px;width:1200px;height:486px;background:var(--dark);clip-path:polygon(0 75px,100% 0,100% 100%,0 100%)}
.foot-brand{left:106px;top:2190px;display:flex;align-items:center;gap:14px;font-size:46px;font-weight:600;color:var(--white)}
.foot-brand .brand-dot{border-color:var(--white);width:46px;height:46px}
.foot-head{color:var(--white);font-size:18.5px;font-weight:500}
.foot-list{list-style:none;color:var(--white);font-size:16.5px;line-height:18px}
.foot-list li{margin-bottom:18px}
.contact li{display:flex;gap:8px;align-items:center}
.rule{left:118px;top:2422px;width:964px;height:1px;background:#555}
.copy{left:112px;top:2452px;color:var(--white);font-size:16.5px}
.social{top:2450px;width:45px;height:45px;border:1px solid #777;border-radius:50%}
</style>
</head>
<body>
<header class="abs header">
  <div class="abs brand"><span class="brand-dot"></span>Pins &amp; Dials</div>
  <nav class="abs nav">
    <a class="active">Agile<br>Coaching</a>
    <a>Coaching @<br>the Team Level</a>
    <a>Coaching @<br>the Program Level</a>
    <a>Mentor<br>Nook</a>
    <a>Reference<br>Materials</a>
  </nav>
</header>

<section class="abs hero" role="img" aria-label="Photo of two colleagues reviewing sticky notes on a glass wall"></section>
<div class="abs hero-kicker">Agile Team Coaching</div>
<h1 class="abs hero-title">Teams working major<br>IT projects, multplue<br>months/years</h1>

<div class="abs eyebrow" style="top:551px">Agile Coaching</div>
<h2 class="abs heading" style="top:585px">The Landscape</h2>

<div class="abs card" style="left:111px;top:690px;width:978px;height:397px"></div>
<div class="abs photo" style="left:111px;top:690px;width:453px;height:397px" role="img" aria-label="Photo of hands typing on a laptop with a holographic task board"></div>
<div class="abs" style="left:612px;top:732px">
  <h3 class="card-title">Multiple Teams Development</h3>
  <ul class="ticks" style="margin-top:20px">
    <li><svg width="15" height="15" viewBox="0 0 16 16"><circle cx="8" cy="8" r="8" fill="#1fc98e"/><path d="M4.5 8.2l2.4 2.3 4.6-4.8" stroke="#fff" stroke-width="2" fill="none"/></svg>Scrum Masters</li>
    <li><svg width="15" height="15" viewBox="0 0 16 16"><circle cx="8" cy="8" r="8" fill="#1fc98e"/><path d="M4.5 8.2l2.4 2.3 4.6-4.8" stroke="#fff" stroke-width="2" fill="none"/></svg>Program Managers</li>
    <li><svg width="15" height="15" viewBox="0 0 16 16"><circle cx="8" cy="8" r="8" fill="#1fc98e"/><path d="M4.5 8.2l2.4 2.3 4.6-4.8" stroke="#fff" stroke-width="2" fill="none"/></svg>Developers</li>
    <li><svg width="15" height="15" viewBox="0 0 16 16"><circle cx="8" cy="8" r="8" fill="#1fc98e"/><path d="M4.5 8.2l2.4 2.3 4.6-4.8" stroke="#fff" stroke-width="2" fill="none"/></svg>Architects</li>
    <li><svg width="15" height="15" viewBox="0 0 16 16"><circle cx="8" cy="8" r="8" fill="#1fc98e"/><path d="M4.5 8.2l2.4 2.3 4.6-4.8" stroke="#fff" stroke-width="2" fill="none"/></svg>Integration Specialists</li>
    <li><svg width="15" height="15" viewBox="0 0 16 16"><circle cx="8" cy="8" r="8" fill="#1fc98e"/><path d="M4.5 8.2l2.4 2.3 4.6-4.8" stroke="#fff" stroke-width="2" fill="none"/></svg>QA Testers</li>
    <li><svg width="15" height="15" viewBox="0 0 16 16"><circle cx="8" cy="8" r="8" fill="#1fc98e"/><path d="M4.5 8.2l2.4 2.3 4.6-4.8" stroke="#fff" stroke-width="2" fill="none"/></svg>UAT Testers</li>
    <li><svg width="15" height="15" viewBox="0 0 16 16"><circle cx="8" cy="8" r="8" fill="#1fc98e"/><path d="M4.5 8.2l2.4 2.3 4.6-4.8" stroke="#fff" stroke-width="2" fill="none"/></svg>IT / IS Stakeholders</li>
  </ul>
</div>

<div class="abs card" style="left:111px;top:1127px;width:978px;height:388px"></div>
<div class="abs photo-light" style="left:637px;top:1127px;width:452px;height:388px" role="img" aria-label="Photo of a handshake over printed business charts"></div>
<div class="abs" style="left:158px;top:1187px">
  <h3 class="card-title">Multiple Teams&nbsp; Business</h3>
  <ul class="ticks" style="margin-top:20px">
    <li><svg width="15" height="15" viewBox="0 0 16 16"><circle cx="8" cy="8" r="8" fill="#1fc98e"/><path d="M4.5 8.2l2.4 2.3 4.6-4.8" stroke="#fff" stroke-width="2" fill="none"/></svg>UAT Testers</li>
    <li><svg width="15" height="15" viewBox="0 0 16 16"><circle cx="8" cy="8" r="8" fill="#1fc98e"/><path d="M4.5 8.2l2.4 2.3 4.6-4.8" stroke="#fff" stroke-width="2" fill="none"/></svg>Business Requirements Analysts</li>
    <li><svg width="15" height="15" viewBox="0 0 16 16"><circle cx="8" cy="8" r="8" fill="#1fc98e"/><path d="M4.5 8.2l2.4 2.3 4.6-4.8" stroke="#fff" stroke-width="2" fill="none"/></svg>Product Owners</li>
    <li><svg width="15" height="15" viewBox="0 0 16 16"><circle cx="8" cy="8" r="8" fill="#1fc98e"/><path d="M4.5 8.2l2.4 2.3 4.6-4.8" stroke="#fff" stroke-width="2" fill="none"/></svg>Product Managers</li>
    <li><svg width="15" height="15" viewBox="0 0 16 16"><circle cx="8" cy="8" r="8" fill="#1fc98e"/><path d="M4.5 8.2l2.4 2.3 4.6-4.8" stroke="#fff" stroke-width="2" fill="none"/></svg>Business Stakeholders</li>
  </ul>
</div>

<div class="abs soft-band"></div>
<div class="abs eyebrow" style="top:1683px">Job</div>
<h2 class="abs heading" style="top:1716px">My Role</h2>

<div class="abs role" style="left:111px;top:1797px;width:464px;height:168px">
  <svg width="120" height="100" viewBox="0 0 120 100" fill="none" stroke="#1fc98e" stroke-width="3">
    <path d="M70 30a28 28 0 1 1-40-4"/><path d="M24 18l6 8-9 4"/>
    <path d="M8 82h60a28 28 0 0 0 20-10"/><path d="M4 88h64"/><path d="M90 74h24"/><path d="M106 66l8 8-8 8"/>
  </svg>
  <p>My role as a technical scrum master and team coach</p>
</div>
<div class="abs role" style="left:624px;top:1797px;width:464px;height:168px">
  <svg width="110" height="110" viewBox="0 0 110 110" fill="none" stroke="#1fc98e" stroke-width="3">
    <circle cx="55" cy="55" r="22"/><circle cx="55" cy="55" r="30" stroke-dasharray="8 6"/>
    <circle cx="55" cy="50" r="6"/><path d="M44 66a11 11 0 0 1 22 0"/>
    <path d="M20 40a38 38 0 0 1 30-26h54"/><path d="M96 6l8 8-8 8"/>
    <path d="M90 70a38 38 0 0 1-30 26H6"/><path d="M14 88l-8 8 8 8"/>
  </svg>
  <p>My job as a business transformation program manager and team coach</p>
</div>

<footer class="abs footer"></footer>
<div class="abs foot-brand"><span class="brand-dot"></span>Pins &amp; Dials</div>

<div class="abs foot-head" style="left:543px;top:2121px">Quick Links</div>
<ul class="abs foot-list" style="left:543px;top:2172px">
  <li>Home</li>
  <li>Agile Team Coaching</li>
  <li>Coaching @ the Team Level</li>
  <li>Coaching @ the Program Level ;<br>LYNQ BQR level</li>
  <li>Mentor Nook</li>
  <li>Contact</li>
</ul>

<div class="abs foot-head" style="left:849px;top:2121px">Contact Us</div>
<ul class="abs foot-list contact" style="left:849px;top:2172px">
  <li><svg width="13" height="13" viewBox="0 0 16 16"><path d="M3 1l3 3-2 2a10 10 0 0 0 6 6l2-2 3 3-2 2C7 15 1 9 1 3z" fill="#1fc98e"/></svg>1 555 010 0188</li>
  <li><svg width="16" height="12" viewBox="0 0 16 12"><rect width="16" height="12" rx="1" fill="#1fc98e"/><path d="M1 1l7 6 7-6" stroke="#222" stroke-width="1.5" fill="none"/></svg>brent.holloway@pinsanddials.example</li>
  <li><svg width="11" height="15" viewBox="0 0 12 16"><path d="M6 0a6 6 0 0 0-6 6c0 4 6 10 6 10s6-6 6-10a6 6 0 0 0-6-6z" fill="#1fc98e"/><circle cx="6" cy="6" r="2" fill="#222"/></svg>Remote Location</li>
</ul>

<div class="abs rule"></div>
<div class="abs copy">Copyright © 2022 Pins and Dials - Agile IT Coaching and Training - all rights reserved.</div>
<div class="abs social" style="left:940px" aria-label="Social link"></div>
<div class="abs social" style="left:991px" aria-label="Social link"></div>
<div class="abs social" style="left:1043px" aria-label="Social link"></div>
</body>
</html>
```